BRIGHTWAVE PARTNERS NAMECARD

Need to design a name card with an existing logo.

As we are professional corporate services provider our name card has to project a professional image.
Should be corporate, simple & professional.

Our corporate color is maroon red but not too dull.

Please refer to our website at www.brightwavepartners.com.sg

Would attach our logo herewith.

Front surface of namecard details:
BRIGHTWAVE PARTNERS PTE LTD
Registration No. 208731945K

Lowe Hui Ting CA (Singapore)
Director

Tel +65 6481 2957
Mobile +65 9172 3806
lowe@brightwavepartners.com.sg
www.brightwavepartners.com.sg

47 Palmer Lane
#07-14 Harbourlight Plaza
Singapore 274153

Back of namecard:-
OUR CORE SERVICES
Incorporation services
Corporate Secretarial Services
Accountancy service
Goods & Services Taxation
Corporate & Personal Taxation
Financial Reporting
Payroll Administration

AFFILIATES:
TRIVANTA CORPORATE SERVICES PTE LTD
BRIGHTWAVEREGISTRYPTE LTD
ORR MANAGEMENT SERVICES PTE LTD
DW LIM AND COMPANY PTE LTD
LEDGERWISE ACADEMY

```html
<!DOCTYPE html>
<html lang="en">
<head>
<meta charset="utf-8">
<title>Brightwave Partners Stationery</title>
<link href="https://fonts.googleapis.com/css2?family=Open+Sans:wght@400;600;700&display=swap" rel="stylesheet">
<style>
  :root {
    --brand-red: #d21f34;
    --charcoal: #333333;
    --paper: #ffffff;
    --backdrop: #e8e6e3;
    --ink: #333333;
  }
  * { margin: 0; padding: 0; box-sizing: border-box; }
  html, body { width: 1200px; height: 1000px; overflow: hidden; }
  body {
    position: relative;
    background: var(--backdrop);
    font-family: "Open Sans", Arial, sans-serif;
    color: var(--ink);
  }
  .sheet {
    position: absolute;
    background: var(--paper);
    box-shadow: 0 2px 8px rgba(0,0,0,0.18);
    overflow: hidden;
  }
  .sheet > svg.shapes { position: absolute; left: 0; top: 0; }
  .wordmark {
    position: absolute;
    font-weight: 700;
    color: var(--brand-red);
    text-transform: uppercase;
    letter-spacing: -0.02em;
    line-height: 1;
  }
  .wordmark span { display: block; }
  .contact-list { position: absolute; list-style: none; color: #fff; }
  .contact-list li { display: flex; align-items: center; white-space: nowrap; }
  .contact-list svg { flex: none; }
  .address { position: absolute; text-align: right; color: var(--ink); line-height: 1.35; }

  /* Letterhead */
  .letterhead { left: 107px; top: 163px; width: 453px; height: 642px; }
  .letterhead .wordmark { left: 20px; top: 22px; font-size: 17px; }
  .letterhead .contact-list { left: 12px; top: 585px; font-size: 6.5px; line-height: 9px; }
  .letterhead .contact-list svg { width: 6px; height: 6px; margin-right: 4px; }
  .letterhead .address { right: 17px; top: 597px; font-size: 6.5px; }

  /* Business card front */
  .card-front { left: 585px; top: 167px; width: 249px; height: 141px; }
  .card-front .id-panel {
    position: absolute; left: 8px; top: 7px; width: 183px; height: 126px;
    background: var(--brand-red); color: #fff; padding: 11px 0 0 12px;
  }
  .card-front .person { font-size: 9px; line-height: 1.15; }
  .card-front .role { font-size: 7.5px; line-height: 1.2; }
  .card-front .card-address { margin-top: 11px; font-size: 5.8px; line-height: 9px; }
  .card-front .contact-list { position: static; margin-top: 9px; font-size: 5.8px; line-height: 9.5px; }
  .card-front .contact-list svg { width: 6px; height: 6px; margin-right: 5px; }
  .card-front .wordmark {
    left: 198px; top: 10px; height: 122px;
    writing-mode: vertical-rl; font-size: 17px; text-align: center;
  }

  /* Business card back */
  .card-back { left: 585px; top: 374px; width: 249px; height: 142px; }
  .card-back .wordmark { left: 13px; top: 15px; font-size: 8.5px; color: var(--charcoal); }
  .card-back .info-panel {
    position: absolute; left: 9px; top: 43px; width: 231px; height: 89px;
    background: var(--charcoal); color: #fff; display: flex; padding: 6px 8px;
  }
  .card-back h3 { font-size: 5.6px; font-weight: 700; line-height: 9px; }
  .card-back ul { list-style: none; font-size: 5.6px; line-height: 8.8px; }
  .card-back .affiliates { width: 129px; }
  .card-back .core-services ul { font-size: 6px; }

  /* Notepad */
  .notepad { left: 861px; top: 165px; width: 252px; height: 356px; }
  .notepad .wordmark { left: 12px; top: 13px; font-size: 9.5px; }
  .notepad .contact-list { left: 9px; top: 324px; font-size: 3.6px; line-height: 5px; }
  .notepad .contact-list svg { width: 3.5px; height: 3.5px; margin-right: 2px; }
  .notepad .address { right: 10px; top: 330px; font-size: 3.6px; line-height: 5px; }

  /* Envelope */
  .envelope { left: 585px; top: 540px; width: 529px; height: 263px; }
  .envelope .wordmark { left: 22px; top: 22px; font-size: 22px; }
  .envelope .address { right: 14px; top: 225px; font-size: 9.5px; line-height: 11px; }
</style>
</head>
<body>

<svg width="0" height="0" style="position:absolute" aria-hidden="true">
  <defs>
    <symbol id="icon-phone" viewBox="0 0 10 10"><path d="M2 0.5h2l1 2.5-1.3 1a6 6 0 0 0 2.3 2.3l1-1.3 2.5 1v2a1.5 1.5 0 0 1-1.5 1.5A8 8 0 0 1 0.5 2 1.5 1.5 0 0 1 2 .5z" fill="currentColor"/></symbol>
    <symbol id="icon-mobile" viewBox="0 0 10 10"><rect x="2.5" y="0.5" width="5" height="9" rx="1" fill="none" stroke="currentColor" stroke-width="1.2"/><circle cx="5" cy="8" r="0.6" fill="currentColor"/></symbol>
    <symbol id="icon-mail" viewBox="0 0 10 10"><rect x="0.5" y="2" width="9" height="6.5" fill="currentColor"/><path d="M0.8 2.3 5 5.6 9.2 2.3" fill="none" stroke="#d21f34" stroke-width="0.9"/></symbol>
    <symbol id="icon-globe" viewBox="0 0 10 10"><circle cx="5" cy="5" r="4.3" fill="none" stroke="currentColor" stroke-width="1"/><path d="M0.7 5h8.6M5 .7c-2.4 2.6-2.4 6 0 8.6M5 .7c2.4 2.6 2.4 6 0 8.6" fill="none" stroke="currentColor" stroke-width="0.8"/></symbol>
  </defs>
</svg>

<!-- Letterhead -->
<section class="sheet letterhead">
  <svg class="shapes" width="453" height="642" viewBox="0 0 453 642" aria-hidden="true">
    <polygon points="306,37 343,0 453,0 453,115 418,150" fill="var(--charcoal)"/>
    <polygon points="0,574 46,528 160,642 0,642" fill="var(--brand-red)"/>
  </svg>
  <div class="wordmark"><span>Brightwave</span><span>Partners</span></div>
  <ul class="contact-list">
    <li><svg><use href="#icon-phone"/></svg>+65 6481 2957</li>
    <li><svg><use href="#icon-mobile"/></svg>+65 9172 3806</li>
    <li><svg><use href="#icon-mail"/></svg>lowe@brightwavepartners.com.sg</li>
    <li><svg><use href="#icon-globe"/></svg>www.brightwavepartners.com.sg</li>
  </ul>
  <address class="address" style="font-style:normal">47 Palmer Lane<br>#07-14 Harbourlight Plaza<br>Singapore 274153</address>
</section>

<!-- Business card, front -->
<section class="sheet card-front">
  <div class="id-panel">
    <p class="person">Lowe Hui Ting CA(Singapore)</p>
    <p class="role">Director</p>
    <p class="card-address">47 Palmer Lane<br>#07-14 Harbourlight Plaza<br>Singapore 274153</p>
    <ul class="contact-list">
      <li><svg><use href="#icon-phone"/></svg>+65 6481 2957</li>
      <li><svg><use href="#icon-mobile"/></svg>+65 9172 3806</li>
      <li><svg><use href="#icon-mail"/></svg>lowe@brightwavepartners.com.sg</li>
      <li><svg><use href="#icon-globe"/></svg>www.brightwavepartners.com.sg</li>
    </ul>
  </div>
  <div class="wordmark"><span>Brightwave</span><span>Partners</span></div>
</section>

<!-- Business card, back -->
<section class="sheet card-back">
  <div class="wordmark"><span>Brightwave</span><span>Partners</span></div>
  <div class="info-panel">
    <div class="affiliates">
      <h3>AFFILIATES</h3>
      <ul>
        <li>TRIVANTA CORPORATE SERVICES PTE LTD</li>
        <li>BRIGHTWAVEREGISTRYPTE LTD</li>
        <li>ORR MANAGEMENT SERVICES PTE LTD</li>
        <li>DW LIM AND COMPANY PTE LTD</li>
        <li>LEDGERWISE ACADEMY</li>
      </ul>
    </div>
    <div class="core-services">
      <h3>Core Services</h3>
      <ul>
        <li>Incorporation Services</li>
        <li>Corporate Secretarial Services</li>
        <li>Accountancy Service</li>
        <li>Goods &amp; Services Taxation</li>
        <li>Corporate &amp; Personal Taxation</li>
        <li>Financial Reporting</li>
        <li>Payroll Administration</li>
      </ul>
    </div>
  </div>
</section>

<!-- Notepad -->
<section class="sheet notepad">
  <svg class="shapes" width="252" height="356" viewBox="0 0 252 356" aria-hidden="true">
    <polygon points="171,35 206,0 252,0 252,48 218,82" fill="var(--charcoal)"/>
    <polygon points="0,325 28,293 91,356 0,356" fill="var(--brand-red)"/>
  </svg>
  <div class="wordmark"><span>Brightwave</span><span>Partners</span></div>
  <ul class="contact-list">
    <li><svg><use href="#icon-phone"/></svg>+65 6481 2957</li>
    <li><svg><use href="#icon-mobile"/></svg>+65 9172 3806</li>
    <li><svg><use href="#icon-mail"/></svg>lowe@brightwavepartners.com.sg</li>
    <li><svg><use href="#icon-globe"/></svg>www.brightwavepartners.com.sg</li>
  </ul>
  <address class="address" style="font-style:normal">47 Palmer Lane<br>#07-14 Harbourlight Plaza<br>Singapore 274153</address>
</section>

<!-- Envelope -->
<section class="sheet envelope">
  <svg class="shapes" width="529" height="263" viewBox="0 0 529 263" aria-hidden="true">
    <polygon points="341,37 378,0 529,0 529,98 466,161" fill="var(--charcoal)"/>
    <polygon points="0,216 46,172 147,263 0,263" fill="var(--brand-red)"/>
  </svg>
  <div class="wordmark"><span>Brightwave</span><span>Partners</span></div>
  <address class="address" style="font-style:normal">47 Palmer Lane<br>#07-14 Harbourlight Plaza<br>Singapore 274153</address>
</section>

</body>
</html>
```